Verdant Loop Advisors, LLC

I am looking for a simple, clear layout with my logo prominent and embossed, on the best quality card stock available. I would like the business name and phone number included on the card as well......I dont want my name anywhere on the card and I would like my logo embossed on the card......something simple with a white back......open to designs as long as they go along with recycling symbols and green type stuff.....The address, website, cell number, fax number, and email are listed below

5374 Tillbury Fenwood Road
Fenbrook, MD 20999

c. 240.555.0143 f. 240.555.0187
e. sales@verdantloopadvisors.example
w. www.verdantloopadvisors.example

Industry/Entity Type

Recycling

```html
<!DOCTYPE html>
<html lang="en">
<head>
<meta charset="utf-8">
<title>Verdant Loop Advisors, LLC — Business Card</title>
<link rel="stylesheet" href="https://fonts.googleapis.com/css2?family=Open+Sans:wght@400;700&display=swap">
<style>
  :root {
    --backdrop: #d9d6d0;
    --leaf-green: #3e8a5a;
    --card-cream: #ebe8de;
    --ink: #3a3a3a;
    --ink-soft: #4a4a4a;
  }
  * { box-sizing: border-box; margin: 0; padding: 0; }
  html, body {
    width: 1200px;
    height: 800px;
    overflow: hidden;
    background: var(--backdrop);
    font-family: "Open Sans", sans-serif;
  }
  .canvas {
    width: 1200px;
    height: 800px;
    display: flex;
    align-items: center;
    justify-content: center;
    gap: 80px;
  }
  .card {
    width: 340px;
    height: 595px;
    position: relative;
    overflow: hidden;
  }
  .card-front {
    background: var(--leaf-green);
    display: flex;
    flex-direction: column;
    align-items: center;
    justify-content: center;
    gap: 26px;
  }
  .front-mark {
    width: 150px;
    height: 150px;
    border-radius: 50%;
    background: var(--card-cream);
  }
  .front-name {
    color: var(--card-cream);
    font-weight: 700;
    font-size: 20px;
    letter-spacing: 0.02em;
    text-align: center;
    line-height: 1.3;
  }
  .card-back {
    background: var(--card-cream);
    padding: 54px 34px 40px 34px;
    display: flex;
    flex-direction: column;
  }
  .brand-line {
    display: flex;
    align-items: center;
    gap: 10px;
  }
  .brand-square {
    width: 18px;
    height: 18px;
    background: var(--leaf-green);
    flex: none;
  }
  .brand-name {
    color: var(--leaf-green);
    font-weight: 700;
    font-size: 14px;
    text-transform: uppercase;
    letter-spacing: 0.02em;
    white-space: nowrap;
  }
  .address {
    margin-top: 118px;
    color: var(--ink);
    font-size: 18px;
    font-style: normal;
    line-height: 1.35;
    text-align: center;
  }
  .contact {
    margin-top: auto;
    color: var(--ink-soft);
    font-size: 12.5px;
    line-height: 1.5;
  }
</style>
</head>
<body>
  <main class="canvas">
    <section class="card card-front" aria-label="Card front">
      <div class="front-mark" aria-hidden="true"></div>
      <p class="front-name">Verdant Loop<br>Advisors, LLC</p>
    </section>

    <section class="card card-back" aria-label="Card back">
      <div class="brand-line">
        <span class="brand-square" aria-hidden="true"></span>
        <span class="brand-name">Verdant Loop Advisors, LLC</span>
      </div>
      <address class="address">
        5374 Tillbury Fenwood Road<br>
        Fenbrook, MD 20999
      </address>
      <p class="contact">
        c. 240.555.0143 &nbsp;f. 240.555.0187<br>
        e. sales@verdantloopadvisors.example<br>
        w. www.verdantloopadvisors.example
      </p>
    </section>
  </main>
</body>
</html>
```